Business Card Design

We are a motorcycle parts, spares, accessories and workshop as well as a vq dealership. We mostly specialize in dirt bikes. I have uploaded a pic of bikes lined up at the starting gate. I envisage having the picture as a backboard maybe out of focus with the logo at the top of the card and the details off to the right side.

Target Market(s)

Male Motorcycle enthusiast aged 18-35

Industry/Entity Type

Business

Contact Information for Business Card

7/318 Banksia Hollow Rd
Wattle Creek QLD 4078
Ph: (07) 3482 9157
Email: maree@trailgearsupply.com.au
www.trailgearsupply.com.au

Requirements
Must have
• on the rear side of the card lines for writing

```html
<!DOCTYPE html>
<html lang="en">
<head>
<meta charset="utf-8">
<title>Kestrel's Business Card</title>
<link rel="stylesheet" href="https://fonts.googleapis.com/css2?family=Open+Sans:wght@400;700&display=swap">
<style>
  :root {
    --stage: #121a1c;
    --card: #ffffff;
    --ink: #1a1a1a;
    --mark-grey: #a7a9ac;
    --rule: #6d6e71;
    --photo-red: #c8323f;
    --photo-blue: #3a4fa8;
    --photo-grey: #8d8f93;
  }
  * { margin: 0; padding: 0; box-sizing: border-box; }
  html, body {
    width: 1200px; height: 801px; overflow: hidden;
    background: var(--stage);
    font-family: "Open Sans", Arial, sans-serif;
  }
  .canvas { position: relative; width: 1200px; height: 801px; background: var(--stage); }

  .card { position: absolute; background: var(--card); overflow: hidden; }

  .card--front { left: 187px; top: 161px; width: 308px; height: 479px; }
  .brand {
    position: absolute; top: 40px; left: 0; width: 100%;
    display: flex; justify-content: center; align-items: center; gap: 10px;
  }
  .brand__name {
    font-weight: 700; font-size: 33px; letter-spacing: 2px;
    color: var(--ink); line-height: 1;
  }
  .brand__square { width: 18px; height: 18px; background: var(--ink); }

  .contact {
    position: absolute; top: 132px; left: 0; width: 100%;
    text-align: center; color: var(--ink);
    font-size: 12.5px; line-height: 14px;
  }
  .contact p + p { margin-top: 13px; }

  .photo {
    position: absolute; left: 0; top: 275px; width: 308px; height: 204px;
    background:
      linear-gradient(to bottom, rgba(255,255,255,1) 0%, rgba(255,255,255,0) 22%),
      linear-gradient(160deg, var(--photo-grey) 0%, var(--photo-red) 45%, var(--photo-grey) 70%, var(--photo-blue) 100%);
  }

  .card--back { left: 535px; top: 332px; width: 477px; height: 308px; }
  .write-line {
    position: absolute; left: 29px; width: 415px;
    border-top: 1px dotted var(--rule);
  }
  .write-line--short { width: 282px; }
  .back-mark {
    position: absolute; left: 322px; top: 261px;
    font-weight: 700; font-size: 20px; letter-spacing: 2.5px;
    color: var(--mark-grey); line-height: 1;
  }
</style>
</head>
<body>
<main class="canvas">
  <section class="card card--front" aria-label="Card front">
    <div class="brand">
      <span class="brand__name">KESTREL'S</span>
      <span class="brand__square"></span>
    </div>
    <div class="contact">
      <p>7/318 Banksia Hollow Rd<br>Wattle Creek QLD 4078</p>
      <p>Ph: (07) 3482 9157</p>
      <p>Email: maree@trailgearsupply.com.au<br>www.trailgearsupply.com.au</p>
    </div>
    <div class="photo" role="img" aria-label="Photo of dirt bikes lined up at a red starting gate under a blue sky"></div>
  </section>

  <section class="card card--back" aria-label="Card back with writing lines">
    <div class="write-line" style="top:63px"></div>
    <div class="write-line" style="top:97px"></div>
    <div class="write-line" style="top:132px"></div>
    <div class="write-line" style="top:166px"></div>
    <div class="write-line" style="top:201px"></div>
    <div class="write-line" style="top:235px"></div>
    <div class="write-line write-line--short" style="top:270px"></div>
    <span class="back-mark">KESTREL'S</span>
  </section>
</main>
</body>
</html>
```